New theme for existing wordpress site

We have an existing website at www.larkfieldmh.com which uses wordpress. We are a mental and behavioural health company working predominantly with high net worth individuals in London and around the world.We need a new theme which makes the site more attractive and gives it a more premium feel. We would like to explore two possible concepts. Either one that uses images of Wrenhollow Lane - as that is where we are based - it is an iconic location with lots of strong visuals. Or one which uses portraits of people. People are key to the work we do. Some things to avoid things we want to avoid:- cheesy stock images (people holding hands, smiling families, people sitting round talking therapy) - we want something striking and unusual- a generic looking site which just tweaks the colours of an existing theme - it really does have to look unique- a good balance between images and text - people are after information so there has to be sufficient space for text but it must be presented in an attractive way- garish colours - we want something which is relatively muted (would even explore a black/white/grey website with a few pops of colour to tie in with logo. No orange please.I have not used sketchhive for this sort of project before so will need an explanation of how you will apply the theme to the existing content on the site.Feel free to use the LMH logo for colour and font inspiration. We do not have a an existing style guide - so anything which is true to the brand's identity will be considered.Please consider using stock images from fotzel, clearsnap and vimorra for your design. If you want images of Wrenhollow Lane these can be supplied.

Target Market(s)

Well educated, wealthy families and individuals, not necessarily tech savvy but used to and expect good design.

Industry/Entity Type

Health And Wellness

Font styles to use
Sans Serif

Colors

Designer to choose colors to be used in the design.

Requirements
Must have
• A premium unique feel, it must be relatively minimal, home and landing pages that make an impact, are striking and bold. Must have strong royalty free imagery. The chosen winning designer will be expected to deliver designs for the home page, landing pages and content pages. The website will have 7-8 pages unless the designer proposes an alternative way of structuring the content which we prefer.
Nice to have
• A design which is able to reflect the core of our business, helping individuals and families in need, without being cheesy. A video landing page could be cool.
• Should be calm, and cool.
• Be good to see a monochrome design with a pop of colour.
Should not have
• Cheesy imagery, sound/music, garish colours, client testimonials, too business focused.

```html
<!DOCTYPE html>
<html lang="en">
<head>
<meta charset="utf-8">
<title>Larkfield Mental Health</title>
<link href="https://fonts.googleapis.com/css2?family=Montserrat:wght@400;500;600;700&display=swap" rel="stylesheet">
<style>
  :root {
    --sky: #3fb1e6;
    --white: #ffffff;
    --ink: #4a4a4a;
    --logo: #3c4a5c;
    --footer: rgba(30, 30, 40, 0.55);
  }
  * { box-sizing: border-box; margin: 0; padding: 0; }
  html, body { width: 1200px; height: 584px; overflow: hidden; }
  body { font-family: "Montserrat", sans-serif; position: relative; }

  .hero-image {
    position: absolute; inset: 0;
    background:
      linear-gradient(rgba(20,20,40,0.28), rgba(20,20,40,0.38)),
      linear-gradient(90deg, #8a5a2a 0%, #b88a3a 14%, #c9706e 30%, #b54f7e 42%, #8a6fa8 55%, #4a86c2 68%, #5aa0c8 80%, #7fa6b8 100%);
  }
  .hero-image::after {
    content: ""; position: absolute; left: 0; top: 0; bottom: 0; width: 32px;
    background: rgba(0,0,0,0.25);
  }

  .site-nav { position: absolute; left: 132px; top: 0; width: 156px; height: 372px; }
  .site-nav svg.nav-shape { position: absolute; inset: 0; }
  .brand {
    position: absolute; left: 0; top: 20px; width: 156px;
    display: flex; flex-direction: column; align-items: center; gap: 8px;
  }
  .brand-dot { width: 30px; height: 30px; border-radius: 50%; background: var(--sky); }
  .brand-name { font-size: 11px; font-weight: 600; color: var(--logo); letter-spacing: 0.5px; text-align: center; line-height: 1.3; }
  .menu { position: absolute; top: 113px; left: 0; width: 156px; list-style: none; }
  .menu li {
    height: 31px; margin-bottom: 10px; display: flex; align-items: center; justify-content: center;
    font-size: 11.5px; font-weight: 500; color: var(--ink); position: relative;
  }
  .menu li.is-active { background: var(--sky); color: var(--white); }
  .menu .caret { position: absolute; right: 18px; top: 13px; }

  .contact-bar { position: absolute; top: 20px; left: 704px; display: flex; align-items: center; gap: 22px; }
  .contact-email { display: flex; align-items: center; gap: 10px; color: var(--white); font-size: 12px; font-weight: 500; white-space: nowrap; }
  .contact-phone {
    display: flex; align-items: center; gap: 9px; height: 35px; padding: 0 15px;
    border-radius: 18px; background: var(--sky); color: var(--white); font-size: 14px; font-weight: 600; letter-spacing: 0.8px; white-space: nowrap;
  }

  .hero-copy { position: absolute; left: 336px; width: 640px; top: 0; height: 584px; color: var(--white); text-align: center; }
  .hero-title {
    position: absolute; left: 0; width: 640px; top: 236px;
    font-size: 42px; font-weight: 700; line-height: 50px; white-space: nowrap;
  }
  .hero-text {
    position: absolute; left: 0; width: 640px; top: 294px;
    font-size: 13.5px; font-weight: 500; line-height: 28px; white-space: nowrap;
  }
  .hero-button {
    position: absolute; left: 237px; top: 364px; width: 192px; height: 45px; line-height: 45px; border-radius: 23px;
    background: var(--sky); color: var(--white); font-size: 14px; font-weight: 700; letter-spacing: 0.3px;
  }

  .slider-dots { position: absolute; top: 446px; left: 638px; display: flex; gap: 19px; }
  .slider-dots span { width: 8px; height: 8px; border-radius: 50%; background: var(--white); }
  .slider-dots span.is-current { background: var(--sky); }

  .site-footer {
    position: absolute; left: 20px; right: 0; top: 548px; height: 16px; background: var(--footer);
    color: var(--white); font-size: 10px; text-align: center; line-height: 16px;
  }
</style>
</head>
<body>
  <div class="hero-image" role="img" aria-label="Street of colourful painted terraced houses with balconies, a lamp post and shopfronts"></div>

  <nav class="site-nav">
    <svg class="nav-shape" width="156" height="372" viewBox="0 0 156 372">
      <polygon points="0,0 156,0 156,344 78,372 0,344" fill="#ffffff"/>
    </svg>
    <div class="brand">
      <span class="brand-dot"></span>
      <span class="brand-name">LARKFIELD<br>MENTAL HEALTH</span>
    </div>
    <ul class="menu">
      <li class="is-active">HOME</li>
      <li>ABOUT US</li>
      <li>OUR SERVICES
        <svg class="caret" width="7" height="5" viewBox="0 0 7 5"><path d="M0.5 0.5 L3.5 3.5 L6.5 0.5" fill="none" stroke="#4a4a4a" stroke-width="1.2"/></svg>
      </li>
      <li>OUR TEAM</li>
      <li>CONATCT US</li>
    </ul>
  </nav>

  <div class="contact-bar">
    <span class="contact-email">
      <svg width="19" height="13" viewBox="0 0 19 13"><rect width="19" height="13" rx="1" fill="#ffffff"/><path d="M1 1 L9.5 7.5 L18 1" fill="none" stroke="#7a6aa0" stroke-width="1.4"/></svg>
      enquiries@larkfieldmh.com
    </span>
    <span class="contact-phone">
      <svg width="12" height="12" viewBox="0 0 24 24"><path d="M6.6 10.8a15.1 15.1 0 0 0 6.6 6.6l2.2-2.2c.3-.3.7-.4 1-.2 1.1.4 2.3.6 3.6.6.6 0 1 .4 1 1V20c0 .6-.4 1-1 1A17 17 0 0 1 3 4c0-.6.4-1 1-1h3.5c.6 0 1 .4 1 1 0 1.3.2 2.5.6 3.6.1.3 0 .7-.2 1z" fill="#ffffff"/></svg>
      020 7946 0382
    </span>
  </div>

  <main class="hero-copy">
    <h1 class="hero-title">Nurturing Body and Mind.</h1>
    <p class="hero-text">Lorem ipsum dolor sit amet facilisis sed vitae lorem pede at eu arcu vulputate<br>metus luctus ut quis vivamus vitae id habitasse et morbi</p>
    <span class="hero-button">SEE OUR SERVICES</span>
  </main>

  <div class="slider-dots"><span></span><span class="is-current"></span><span></span></div>

  <footer class="site-footer">All content of this website is copyright of Larkfield Mental Health Ltd</footer>
</body>
</html>
```